Web Design Project

We are an online tax Continuing education provider. We provide online courses for tax preparers. We want the front end page to be user friendly and for the buyer to know exactly what they are looking at. We want a front end page to look smiliar www.marlowfiling.com. It should have a similar feel to this one.
Our website address will be www.7382QL.com
We currently have another website that is www.LedgerRJs.com but we do not want it to look like this. We want a different look but same information.
We have a logo already which is attached. We don't have specific colors in mind for the front page but don't want it to be too busy looking. It should stand out but not too simple either.
Target Market(s)
Tax Preparers. More serious and professional but these folks are usually not tech savy. Simple, easy to use, and functional is key.
Industry/Entity Type
Education
Requirements
Must have
- Use standard HTML & CSS. NO other coding is needed.
We are looking for 5-7 pages including Home page, log in, FAQ.
Please look at our current website www.LedgerRJs.com and also www.marlowfiling.com

```html
<!DOCTYPE html>
<html lang="en">
<head>
<meta charset="utf-8">
<title>7382QL – Tax Preparer Continuing Education</title>
<link rel="stylesheet" href="https://fonts.googleapis.com/css2?family=Alegreya+Sans+SC:wght@400;500&family=Yanone+Kaffeesatz:wght@300;400;600&display=swap">
<style>
:root{
  --navy-deep:#0c2342;
  --navy:#1a3d6b;
  --navy-glow:#2f5a8e;
  --nav-text:#a8b8cc;
  --intro-text:#bfcbdb;
  --card-top:#ffffff;
  --card-bottom:#dcdfe8;
  --card-title:#4d6a93;
  --card-text:#1f2c48;
  --btn-top:#f6ecc6;
  --btn-bottom:#eed7a6;
  --btn-text:#e8742a;
  --footer-top:#3b6591;
  --footer-bottom:#7da3c8;
  --footer-text:#1c3556;
  --arrow:#9acd32;
}
*{margin:0;padding:0;box-sizing:border-box}
html,body{width:1200px;height:992px;overflow:hidden}
body{
  position:relative;
  font-family:"Alegreya Sans SC",sans-serif;
  background:
    radial-gradient(ellipse 700px 420px at 690px 240px,var(--navy-glow),transparent 70%),
    linear-gradient(var(--navy) 0,var(--navy-deep) 763px);
}
.site-header{position:absolute;left:0;top:0;width:1200px;height:140px}
.nav-link{position:absolute;top:50px;font-size:24px;color:var(--nav-text);text-decoration:none;letter-spacing:.3px;text-shadow:0 1px 2px #061428}
.nav-rule{position:absolute;top:97px;height:1px;background:linear-gradient(90deg,transparent,#8fa8c8,transparent)}
.brand-badge{position:absolute;left:598px;top:0;width:176px;height:140px}
.brand-name{position:absolute;left:598px;top:52px;width:176px;text-align:center;font-family:"Yanone Kaffeesatz",sans-serif;font-weight:600;font-size:30px;color:#e3b548}
.intro{position:absolute;left:240px;width:900px;text-align:center;color:var(--intro-text);font-size:15.5px;line-height:19px}
.testimonials-tab{position:absolute;left:0;top:312px;width:190px;height:48px}
.testimonials-title{position:absolute;left:0;top:322px;width:176px;text-align:center;font-family:"Yanone Kaffeesatz",sans-serif;font-variant:small-caps;font-size:24px;color:#b9c8db}
.testimonials{position:absolute;left:17px;top:399px;width:174px;color:#a9bad0;font-size:13px;line-height:15px;text-align:justify}
.testimonials p{margin-bottom:16px}
.testimonials .author{font-style:italic}
.course-card{position:absolute;top:309px;width:300px;height:346px;border-radius:6px;background:linear-gradient(var(--card-top),var(--card-bottom));box-shadow:0 2px 8px rgba(0,0,0,.45);text-align:center;color:var(--card-text)}
.course-title{font-family:"Yanone Kaffeesatz",sans-serif;font-variant:small-caps;font-weight:300;font-size:26px;line-height:28px;color:var(--card-title);margin:20px 20px 0}
.course-links{position:absolute;left:14px;right:14px;font-size:13px;line-height:15px}
.course-links p{margin-bottom:14px}
.go{display:inline-block;width:0;height:0;border-left:9px solid var(--arrow);border-top:6px solid transparent;border-bottom:6px solid transparent;margin-left:6px;vertical-align:-1px}
.register-btn{position:absolute;left:53px;top:279px;width:190px;height:56px;border-radius:3px;background:linear-gradient(var(--btn-top),var(--btn-bottom));box-shadow:0 1px 3px rgba(0,0,0,.3);font-family:"Yanone Kaffeesatz",sans-serif;font-variant:small-caps;font-weight:600;color:var(--btn-text);line-height:56px;font-size:22px}
.register-btn .price{font-size:30px}
.site-footer{position:absolute;left:0;top:763px;width:1200px;height:229px;background:linear-gradient(170deg,var(--footer-top),var(--footer-bottom));border-top:1px solid #5d82aa}
.irs-box{position:absolute;left:18px;top:17px;width:168px;height:197px;border-radius:4px;background:linear-gradient(#fff,#d7dbe3);box-shadow:0 1px 4px rgba(0,0,0,.4);text-align:center;color:var(--footer-text)}
.irs-box h2{font-family:"Yanone Kaffeesatz",sans-serif;font-variant:small-caps;font-weight:400;font-size:23px;margin-top:22px}
.irs-box small{display:block;font-size:13px;line-height:14px;margin-top:8px}
.bulletin-btn{position:absolute;left:10px;top:126px;width:147px;height:57px;border-radius:4px;background:linear-gradient(#6d8caf,#3f5f85);border:2px solid #2b4566;color:#e6edf6;font-family:"Yanone Kaffeesatz",sans-serif;font-size:19px;line-height:20px;padding-top:7px}
.features{position:absolute;left:230px;top:19px;list-style:none;color:var(--footer-text);font-size:13px}
.features li{height:33.5px}
.features li::before{content:"• "}
.accreditor-badge{position:absolute;left:865px;top:24px;width:211px;height:49px;background:#f2f2f0;border-left:50px solid #8e8f86}
.secure-badge{position:absolute;left:865px;top:95px;width:88px;height:49px;background:#e8c14a;border:2px solid #2a2a2a}
.partner-name{position:absolute;left:865px;top:170px;font-family:"Alegreya Sans SC",sans-serif;font-weight:400;font-size:24px;color:var(--footer-text)}
</style>
</head>
<body>
<header class="site-header">
  <div class="nav-rule" style="left:280px;width:330px"></div>
  <div class="nav-rule" style="left:765px;width:330px"></div>
  <a class="nav-link" style="left:215px">800-555-0142</a>
  <a class="nav-link" style="left:386px">Home</a>
  <a class="nav-link" style="left:478px">Courses</a>
  <a class="nav-link" style="left:836px">FAQ</a>
  <a class="nav-link" style="left:916px">Contact Us</a>
  <a class="nav-link" style="left:1066px">Sign In</a>
  <svg class="brand-badge" viewBox="0 0 176 140" aria-hidden="true">
    <defs><linearGradient id="badgeFill" x1="0" y1="0" x2="0" y2="1"><stop offset="0" stop-color="#28497a"/><stop offset="1" stop-color="#13294b"/></linearGradient></defs>
    <path d="M10 0 H166 L160 110 Q140 118 170 134 Q88 124 6 134 Q36 118 16 110 Z" fill="url(#badgeFill)" stroke="#7f9cc2" stroke-width="2"/>
  </svg>
  <div class="brand-name">7382QL</div>
</header>

<p class="intro" style="top:198px">We are your official source for IRS Registered Tax Preparer CE training. Our prices are reasonable, and our courses will help you better understand taxes in an efficient manner.</p>
<p class="intro" style="top:256px">Quality courses that fulfill IRS registered tax-preparer requirements.</p>

<svg class="testimonials-tab" viewBox="0 0 190 48" aria-hidden="true">
  <path d="M0 2 H188 L176 24 L188 46 H0 Z" fill="#1b3a64" stroke="#5b7ea8" stroke-width="2"/>
</svg>
<div class="testimonials-title">Testimonials</div>
<div class="testimonials">
  <p>Great reading materials! I learned a lot that I did not know previously. I'm so glad I chose your program!!!!!</p>
  <p class="author">-Dana.AK</p>
  <p>The class was very convenient because I work crazy hours ... the pace was great. I learned some laws that I wasn't aware of to help my clients. I highly recommend this course to others. Thank you!!</p>
  <p class="author">-Renee.Tx</p>
</div>

<section class="course-card" style="left:207px">
  <h2 class="course-title">15 Hour Package for IRS Registered TAX Preparer CE</h2>
  <div class="course-links" style="top:124px">
    <p>15-Hour package for IRS Registered Tax-Preparer Continuing Education<span class="go"></span></p>
    <p>More Information about 15-Hour CE package<span class="go"></span></p>
    <p style="font-size:12px;line-height:14px">This package meets the following IRS requirements for registered tax-preparer continuing education: 15-hour per year (beginning in calendar year 2013)<span class="go"></span></p>
  </div>
  <div class="register-btn"><span class="price">$42</span> - Click to Register</div>
</section>

<section class="course-card" style="left:536px">
  <h2 class="course-title">RTRP Exam Preparation Course 10 CE Credit</h2>
  <div class="course-links" style="top:132px">
    <p>Test Simulator Course Details<span class="go"></span></p>
  </div>
  <div class="register-btn"><span class="price">$79.90</span> - Register</div>
</section>

<section class="course-card" style="left:865px">
  <h2 class="course-title">Combo Package RTRP Exam Prep Course and CE<br>- 15 hours CE credit -</h2>
  <div class="course-links" style="top:132px">
    <p>Test Simulator Course Details<span class="go"></span></p>
    <p style="font-size:12px;line-height:15px">5-Hour package of Ethics and Federal Law updates for IRS Registered Tax-Preparer Continuing Education<span class="go"></span></p>
  </div>
  <div class="register-btn"><span class="price">$99.90</span> - Register</div>
</section>

<footer class="site-footer">
  <div class="irs-box">
    <h2>IRS Latest Information</h2>
    <small>(Click button to open IRS document or link)</small>
    <div class="bulletin-btn">RTRP Test Candidate Information Bulletin</div>
  </div>
  <ul class="features">
    <li>We are your official source for registered tax-preparer continuing education.</li>
    <li>IRS-approved provider (Provider Id 7QLRJ).</li>
    <li>Easy to understand</li>
    <li>Relevant, up-to-date materials</li>
    <li>Printable Certificate of Completion</li>
    <li>We report CE hours directly to IRS after completion</li>
  </ul>
  <div class="accreditor-badge" role="img" aria-label="Approved continuing education accreditor badge"></div>
  <div class="secure-badge" role="img" aria-label="Secure connection badge"></div>
  <div class="partner-name">LedgerRJs.com</div>
</footer>
</body>
</html>
```